Web Design for Financial Consulting Company

We need a website design for a financial consulting company "Kelvane Consulting". We build financial models, scenario analysis, handle the budgeting process and provide temporary staffing. I have over 10 years of experience. My Excel expertise and analytical savvy has saved clients over $17 million in profit.

Target Market(s)

Small to medium businesses

Industry/Entity Type

Financial Consulting

Number of Pages Required

4 page

Requirements
Must have
• Professional looking
Nice to have
• A little futuristic looking

```html
<!DOCTYPE html>
<html lang="en">
<head>
<meta charset="utf-8">
<title>Kelvane Consulting</title>
<link rel="stylesheet" href="https://fonts.googleapis.com/css2?family=Montserrat:ital,wght@0,300;0,400;0,500;0,600;0,700;0,800;1,700&display=swap">
<style>
:root{
  --navy:#0f3b62;
  --blue:#17a3ee;
  --ink:#2d3a45;
  --muted:#7a8590;
  --soft:#eef3f8;
  --line:#c9d3dc;
  --footer:#1b2631;
  --white:#ffffff;
}
*{margin:0;padding:0;box-sizing:border-box}
html,body{width:1200px;height:4695px;overflow:hidden}
body{font-family:"Montserrat",sans-serif;color:var(--ink);background:var(--white);position:relative}
.section{position:absolute;left:0;width:1200px;overflow:hidden}
.abs{position:absolute}
.eyebrow{font-size:24px;font-weight:500;color:#3c4650}
.title{font-size:42px;font-weight:800;color:var(--navy);letter-spacing:.5px;line-height:1.2}
.title .light{font-weight:300;color:var(--blue)}
.center{text-align:center;width:1200px;left:0}

/* hero */
.hero{top:0;height:695px;background:radial-gradient(ellipse at 70% 70%,#1c6ad6 0%,#0b2f78 35%,#04112b 70%,#020814 100%)}
.brand{top:42px;left:111px;display:flex;align-items:center;gap:14px}
.brand .mark{width:26px;height:26px;background:var(--blue)}
.brand .name{font-size:30px;font-weight:700;color:var(--white);letter-spacing:2px;line-height:1}
.brand .sub{font-size:14px;font-weight:500;color:var(--blue);letter-spacing:13px;margin-top:6px}
.nav{top:58px;left:675px;display:flex;gap:34px;font-size:17px;font-weight:600;color:var(--white)}
.nav .active{color:var(--blue)}
.hero h1{top:192px;left:108px;font-size:47px;font-weight:800;color:var(--white);line-height:60px;letter-spacing:1px}
.hero-cut{right:0;bottom:0}

/* goals */
.goals{top:695px;height:500px}
.goals .eyebrow{top:68px;left:110px}
.goals .title{top:102px;left:110px}
.goals p{top:225px;left:110px;width:490px;font-size:15px;line-height:27px;color:var(--muted)}
.btn{top:365px;left:111px;width:161px;height:53px;border-radius:27px;background:var(--blue);color:var(--white);font-size:17px;font-weight:700;display:flex;align-items:center;justify-content:center}
.promise-head{top:70px;left:666px;font-size:25px;font-weight:500;color:#2f3a44}
.promise{left:660px;display:flex;align-items:center;gap:22px;font-size:17px;color:#4a5560}
.ring{width:70px;height:70px;border-radius:50%;border:1.5px solid var(--line);display:flex;align-items:center;justify-content:center;background:var(--white)}

/* services */
.services{top:1195px;height:777px;background:var(--soft)}
.service{width:240px;text-align:center}
.service .disc{width:192px;height:192px;margin:0 auto;border-radius:50%;background:var(--white);display:flex;align-items:center;justify-content:center;box-shadow:0 4px 14px rgba(15,59,98,.06)}
.service h3{font-size:22px;font-weight:600;color:var(--ink);line-height:27px;margin-top:22px}
.service p{font-size:15px;line-height:23px;color:var(--muted);margin-top:10px;padding:0 18px}

/* why */
.why{top:1972px;height:569px}
.why-art{left:0;top:0;width:472px;height:569px;background:radial-gradient(ellipse at 55% 55%,#2a6ff0 0%,#0e3aa8 40%,#061a4d 75%,#040f2e 100%)}
.why .eyebrow{top:54px;left:531px}
.why .title{top:94px;left:528px}
.why p{top:170px;left:531px;width:500px;font-size:15px;line-height:27px;color:var(--muted)}
.stat{display:flex;align-items:center;gap:18px}
.stat .ring{width:110px;height:110px}
.stat b{display:block;font-size:27px;font-weight:600;color:#2f3a44}
.stat span{display:block;font-size:15px;color:var(--muted);line-height:23px;width:110px}

/* team */
.team{top:2541px;height:651px;background:var(--soft)}
.team .eyebrow{top:74px}
.team .title{top:118px}
.member{top:215px;width:236px;text-align:center}
.member .photo{height:277px;background:linear-gradient(180deg,#e4e9ee,#cfd6dc)}
.member h4{font-size:21px;font-weight:600;color:#2f3a44;margin-top:30px}
.member span{font-size:15px;color:var(--muted);display:block;margin-top:8px}

/* quote */
.quote{top:3192px;height:368px;background:linear-gradient(100deg,#071a33 0%,#0b2c57 45%,#0f4fa0 75%,#1479d6 100%)}
.quote blockquote{top:67px;left:116px;width:520px;font-size:34px;font-weight:700;font-style:italic;line-height:43px;color:var(--white)}
.quote cite{top:270px;left:116px;font-style:normal;font-size:21px;color:var(--white)}

/* blog */
.blog{top:3560px;height:664px}
.blog .eyebrow{top:66px}
.blog .title{top:112px}
.post{top:205px;width:312px}
.post .img{height:235px}
.post .cat{font-size:16px;color:var(--blue);margin-top:28px}
.post h5{font-size:21px;font-weight:600;color:#2f3a44;line-height:28px;margin-top:6px}
.post .meta{font-size:15px;color:var(--muted);margin-top:14px;display:flex;align-items:center;gap:6px}
.post.faded{opacity:.3}

/* footer */
.footer{top:4224px;height:471px;background:var(--footer);color:var(--white)}
.footer .brand{top:120px;left:262px}
.contact{left:264px;display:flex;gap:10px;font-size:16px;line-height:22px}
.links-head{top:108px;left:726px;font-size:19px;font-weight:500}
.links{font-size:16px;line-height:31px}
.rule{top:385px;left:111px;width:978px;height:1px;background:#3a4652}
.copy{top:419px;left:111px;font-size:15px}
.social{width:48px;height:48px;border-radius:50%;border:1.5px solid var(--blue);top:403px}
</style>
</head>
<body>

<header class="section hero">
  <div class="abs" role="img" aria-label="Glowing blue financial candlestick chart" style="left:420px;top:230px;width:780px;height:465px;background:linear-gradient(180deg,rgba(23,163,238,0) 0%,rgba(23,120,238,.35) 60%,rgba(40,170,255,.55) 100%)"></div>
  <div class="abs brand">
    <div class="mark"></div>
    <div><div class="name">KELVANE</div><div class="sub">CONSULTING</div></div>
  </div>
  <nav class="abs nav"><span class="active">HOME</span><span>ABOUT</span><span>SERVICES</span><span>CONTACT</span></nav>
  <h1 class="abs">HELPING YOUR<br>FINANCE TEAM<br>AND INCREASING<br>PROFIT</h1>
  <svg class="abs hero-cut" width="560" height="280" viewBox="0 0 560 280"><polygon points="0,280 560,0 560,280" fill="#ffffff"/></svg>
</header>

<section class="section goals">
  <div class="abs eyebrow">Our goals</div>
  <h2 class="abs title">WE BRING<br><span class="light">PEOPLE TOGETHER</span></h2>
  <p class="abs">Our goal is to bring people together by breaking down barriers of race, religion, gender, and nationality. We should be striving to promote a world without borders – one where everyone is able to pursue their dreams.</p>
  <div class="abs btn">READ MORE</div>
  <div class="abs promise-head">Our Promise To You</div>
  <div class="abs promise" style="top:116px"><div class="ring"><svg width="34" height="34" viewBox="0 0 34 34"><circle cx="17" cy="17" r="14" fill="none" stroke="#17a3ee" stroke-width="3"/><path d="M17 9v9h6" fill="none" stroke="#17a3ee" stroke-width="3"/></svg></div>Save time and energy</div>
  <div class="abs promise" style="top:195px"><div class="ring"><svg width="34" height="34" viewBox="0 0 34 34"><path d="M5 22v-5a12 12 0 0 1 24 0v5" fill="none" stroke="#17a3ee" stroke-width="3"/><rect x="3" y="19" width="7" height="10" rx="2" fill="#17a3ee"/><rect x="24" y="19" width="7" height="10" rx="2" fill="#17a3ee"/></svg></div>Great support &amp; services</div>
  <div class="abs promise" style="top:273px"><div class="ring"><svg width="34" height="34" viewBox="0 0 34 34"><polygon points="17,3 32,30 2,30" fill="#17a3ee"/><rect x="15.5" y="12" width="3" height="10" fill="#fff"/><rect x="15.5" y="24" width="3" height="3" fill="#fff"/></svg></div>Risk reduction</div>
  <div class="abs promise" style="top:352px"><div class="ring"><svg width="34" height="34" viewBox="0 0 34 34"><circle cx="17" cy="17" r="14" fill="none" stroke="#17a3ee" stroke-width="3"/><path d="M10 17l5 5 9-10" fill="none" stroke="#17a3ee" stroke-width="3"/></svg></div>Peace of mind</div>
</section>

<section class="section services">
  <div class="abs eyebrow center" style="top:54px">Services</div>
  <h2 class="abs title center" style="top:96px">WHAT <span class="light">WE DO</span></h2>

  <div class="abs service" style="left:90px;top:186px">
    <div class="disc"><svg width="96" height="96" viewBox="0 0 96 96" fill="none" stroke="#0f3b62" stroke-width="3"><path d="M36 60a22 22 0 1 1 24 0v10H36z"/><path d="M38 78h20M40 86h16" stroke="#17a3ee"/><path d="M48 30v22M42 36h10a5 5 0 0 1 0 10H44" stroke="#17a3ee"/></svg></div>
    <h3>Financial<br>Models</h3>
    <p>Financial analysis, scenario modeling, pricing analysis, projects</p>
  </div>
  <div class="abs service" style="left:285px;top:330px">
    <div class="disc"><svg width="96" height="96" viewBox="0 0 96 96" fill="none" stroke="#0f3b62" stroke-width="3"><circle cx="48" cy="48" r="34"/><circle cx="48" cy="48" r="22" stroke="#17a3ee"/><path d="M54 38h-9a5 5 0 0 0 0 10h6a5 5 0 0 1 0 10h-10M48 32v32" stroke="#17a3ee"/></svg></div>
    <h3>Budgeting<br>Process</h3>
    <p>Building budgets from scratch, revamping current process to be more robust and scalable.</p>
  </div>
  <div class="abs service" style="left:480px;top:186px">
    <div class="disc"><svg width="96" height="96" viewBox="0 0 96 96" fill="none" stroke="#0f3b62" stroke-width="3"><circle cx="52" cy="44" r="34"/><path d="M52 18v26l16 10" stroke="#17a3ee"/><circle cx="26" cy="70" r="8" stroke="#17a3ee"/></svg></div>
    <h3>Temporary<br>Staffing</h3>
    <p>Years of Financial Planning and Analysis experience across multiple industries can help temporary staffing needs.</p>
  </div>
  <div class="abs service" style="left:675px;top:330px">
    <div class="disc"><svg width="96" height="96" viewBox="0 0 96 96" fill="none" stroke="#0f3b62" stroke-width="3"><ellipse cx="48" cy="22" rx="30" ry="9"/><path d="M18 22v52c0 5 13 9 30 9s30-4 30-9V22"/><path d="M18 40c0 5 13 9 30 9s30-4 30-9M18 57c0 5 13 9 30 9s30-4 30-9" stroke="#17a3ee"/></svg></div>
    <h3>Data<br>cleansing</h3>
    <p>Financial analysis, scenario modeling, pricing analysis, projects</p>
  </div>
  <div class="abs service" style="left:870px;top:186px">
    <div class="disc"><svg width="96" height="96" viewBox="0 0 96 96" fill="none" stroke="#0f3b62" stroke-width="3"><circle cx="34" cy="66" r="10"/><circle cx="62" cy="62" r="14"/><path d="M20 44V24M12 32l8-8 8 8M44 40V16M36 24l8-8 8 8M72 38V12M64 20l8-8 8 8" stroke="#17a3ee"/></svg></div>
    <h3>Process<br>Improvement</h3>
    <p>Month end close, reporting, budgeting</p>
  </div>
</section>

<section class="section why">
  <div class="abs why-art" role="img" aria-label="Blue stock market chart with rising bars and price labels"></div>
  <div class="abs eyebrow">Why choose us</div>
  <h2 class="abs title">30 YEARS <span class="light">OF EXPERIENCE</span></h2>
  <p class="abs">We have been working in this field for 30 years and we are really excited to move forward with more new things.</p>
  <div class="abs stat" style="left:525px;top:253px"><div class="ring"><svg width="40" height="40" viewBox="0 0 40 40"><rect x="4" y="12" width="32" height="22" rx="3" fill="#17a3ee"/><rect x="14" y="6" width="12" height="8" rx="2" fill="none" stroke="#17a3ee" stroke-width="3"/></svg></div><div><b>23876</b><span>Successful Clients</span></div></div>
  <div class="abs stat" style="left:824px;top:253px"><div class="ring"><svg width="40" height="40" viewBox="0 0 40 40"><circle cx="16" cy="22" r="9" fill="none" stroke="#17a3ee" stroke-width="5" stroke-dasharray="4 3"/><circle cx="30" cy="11" r="6" fill="none" stroke="#17a3ee" stroke-width="4" stroke-dasharray="3 2"/></svg></div><div><b>1208</b><span>Ongoing Project</span></div></div>
  <div class="abs stat" style="left:525px;top:388px"><div class="ring"><svg width="40" height="40" viewBox="0 0 40 40"><path d="M12 16a8 8 0 1 1 16 0c0 5-4 7-4 12h-8c0-5-4-7-4-12z" fill="none" stroke="#17a3ee" stroke-width="3"/><path d="M16 33h8M17 37h6" stroke="#17a3ee" stroke-width="3"/></svg></div><div><b>23900</b><span>Successful Strategies</span></div></div>
  <div class="abs stat" style="left:824px;top:388px"><div class="ring"><svg width="40" height="40" viewBox="0 0 40 40"><path d="M4 6v30h32" fill="none" stroke="#17a3ee" stroke-width="3"/><path d="M9 29l8-9 6 5 11-12" fill="none" stroke="#17a3ee" stroke-width="3"/></svg></div><div><b>234965</b><span>Successful Investments</span></div></div>
</section>

<section class="section team">
  <div class="abs eyebrow center">Our Team</div>
  <h2 class="abs title center">PEOPLE YOU <span class="light">CAN TRUST</span></h2>
  <div class="abs member" style="left:111px"><div class="photo" role="img" aria-label="Staff portrait placeholder"></div><h4>Staff Name</h4><span>Lorem Ipisum sert</span></div>
  <div class="abs member" style="left:358px"><div class="photo" role="img" aria-label="Staff portrait placeholder"></div><h4>Staff Name</h4><span>Lorem Ipisum sert</span></div>
  <div class="abs member" style="left:605px"><div class="photo" role="img" aria-label="Staff portrait placeholder"></div><h4>Staff Name</h4><span>Lorem Ipisum sert</span></div>
  <div class="abs member" style="left:852px"><div class="photo" role="img" aria-label="Staff portrait placeholder"></div><h4>Staff Name</h4><span>Lorem Ipisum sert</span></div>
</section>

<section class="section quote" role="img" aria-label="Rising blue arrows over a financial chart backdrop">
  <blockquote class="abs">“We believe that by empowering ourselves, we can empower the world around us.”</blockquote>
  <cite class="abs">John Doe – SEO</cite>
</section>

<section class="section blog">
  <div class="abs eyebrow center">From The Blog</div>
  <h2 class="abs title center">OUR LATEST <span class="light">POSTS</span></h2>
  <article class="abs post" style="left:111px"><div class="img" role="img" aria-label="Growth chart glowing above a tablet" style="background:linear-gradient(160deg,#0a2a66,#1a6fd8)"></div><div class="cat">Finance</div><h5>Top 5 Tips for Financial Success</h5><div class="meta"><svg width="14" height="14"><rect x="1" y="2" width="12" height="11" fill="none" stroke="#7a8590" stroke-width="1.5"/></svg>18/07/2023 | <svg width="12" height="14"><circle cx="6" cy="4" r="3.5" fill="#17a3ee"/><rect x="1" y="9" width="10" height="5" rx="2" fill="#17a3ee"/></svg>Admin</div></article>
  <article class="abs post" style="left:445px"><div class="img" role="img" aria-label="Candlestick chart over a world map" style="background:linear-gradient(160deg,#0c2a4f,#1d5a9e)"></div><div class="cat">Finance</div><h5>Top 5 Tips for Financial Success</h5><div class="meta"><svg width="14" height="14"><rect x="1" y="2" width="12" height="11" fill="none" stroke="#7a8590" stroke-width="1.5"/></svg>18/07/2023 | <svg width="12" height="14"><circle cx="6" cy="4" r="3.5" fill="#17a3ee"/><rect x="1" y="9" width="10" height="5" rx="2" fill="#17a3ee"/></svg>Admin</div></article>
  <article class="abs post" style="left:777px"><div class="img" role="img" aria-label="Glowing city skyline made of data bars" style="background:linear-gradient(160deg,#061a3a,#0f57b8)"></div><div class="cat">Finance</div><h5>Top 5 Tips for Financial Success</h5><div class="meta"><svg width="14" height="14"><rect x="1" y="2" width="12" height="11" fill="none" stroke="#7a8590" stroke-width="1.5"/></svg>18/07/2023 | <svg width="12" height="14"><circle cx="6" cy="4" r="3.5" fill="#17a3ee"/><rect x="1" y="9" width="10" height="5" rx="2" fill="#17a3ee"/></svg>Admin</div></article>
  <article class="abs post faded" style="left:1109px"><div class="img" role="img" aria-label="Pale blue financial chart" style="background:linear-gradient(160deg,#9fc6f0,#3e8fe0)"></div><div class="cat">Finance</div><h5>Top 5 Tips for Financial Success</h5><div class="meta">18/07/2023</div></article>
</section>

<footer class="section footer">
  <svg class="abs" style="left:0;top:0" width="300" height="280" viewBox="0 0 300 280"><polygon points="0,0 300,0 0,280" fill="#ffffff"/></svg>
  <div class="abs brand">
    <div class="mark"></div>
    <div><div class="name">KELVANE</div><div class="sub">CONSULTING</div></div>
  </div>
  <div class="abs contact" style="top:216px"><svg width="12" height="16" viewBox="0 0 12 16"><path d="M6 0a6 6 0 0 1 6 6c0 4-6 10-6 10S0 10 0 6a6 6 0 0 1 6-6z" fill="#17a3ee"/><circle cx="6" cy="6" r="2" fill="#1b2631"/></svg><span>No 1234 emo enim ipsam uptatem<br>quia voluptas 23456</span></div>
  <div class="abs contact" style="top:282px"><svg width="14" height="14" viewBox="0 0 14 14"><path d="M3 0l3 3-2 2c1 2 3 4 5 5l2-2 3 3-2 3C6 14 0 8 0 2z" fill="#17a3ee"/></svg><span>1 888 888 8888</span></div>
  <div class="abs contact" style="top:326px"><svg width="16" height="12" viewBox="0 0 16 12"><rect width="16" height="12" rx="1" fill="#17a3ee"/><path d="M0 1l8 6 8-6" fill="none" stroke="#1b2631" stroke-width="1.5"/></svg><span>info@kelvaneconsulting.com</span></div>
  <div class="abs links-head">Quick Links</div>
  <div class="abs links" style="top:150px;left:726px">Home<br>About<br>Services<br>Contact</div>
  <div class="abs links" style="top:150px;left:865px">Privacy Policy<br>Terms &amp; Conditions</div>
  <div class="abs rule"></div>
  <div class="abs copy">© Kelvane Consulting, 2023. All Rights Reserved.</div>
  <div class="abs social" style="left:924px" aria-label="Social profile"></div>
  <div class="abs social" style="left:981px" aria-label="Social profile"></div>
  <div class="abs social" style="left:1039px" aria-label="Social profile"></div>
</footer>

</body>
</html>
```